Brazilian wine business need a label for a sparkling wine

We are importing a new italian sparkling wine, but we need to build our own brand. Our main focus is to sell sparkling wine for events, specially for weddings. So, specially for this audience, presentation is key.
We like to see wine in a "uncomplicated" way.
It is a mid price product.
The foil capsule color must be black, white or silver, due to production restrictions. We cannot have any graphic interference in this part, also.

We need to develop a label for it. The name will be "Lucenti Brut" (means "hug" in italian).

Our main public is people around the early 30s, so it should look modern and clean.
It is good, but not mandatory, to have a few information at the front label:
- Alcohol % (12%)
- Origin (Italy)

We need to avoid a few colours, for different reasons:
- Don´t use yellow/orange: too linked to Maison Dorvalle;
- Don´t use red or pink: people think it is a rosé, but it is a white.
Our idea is to work with white and blue or turquoise, maybe a green, something like that. Can have a touch of gold, also. (more references in the color tab below)
- The bottle is black.

Industry/Entity Type

Business

Font styles to use
Other font styles liked:
• Berlin Sans FB Regular or something less "round" but similar to Cooper Black Regular

Colors
00a990
33b8a4

Requirements
Must have
• As the name means "hug", we want to have a graphic symbol that represents connections, alliances, symbiosis or infinite. I attached a few symbols that could be explore, but of course you can bring differente suggestions.
• We need a clean design, nothing with too many information.

```html
<!DOCTYPE html>
<html lang="en">
<head>
<meta charset="utf-8">
<title>Lucenti Brut – Label Variants</title>
<link rel="stylesheet" href="https://fonts.googleapis.com/css2?family=Josefin+Slab:wght@300;400&family=Raleway:wght@300;400&display=swap">
<style>
  :root {
    --canvas-bg: #ffffff;
    --label-blue: #0f74c1;
    --label-teal: #0dba9a;
    --silver-light: #f2f2f2;
    --silver-mid: #c4c4c4;
    --silver-dark: #8f8f8f;
    --band-grey: #a9a9a9;
    --text-white: #ffffff;
    --text-silver: #e6e6e6;
  }
  * { margin: 0; padding: 0; box-sizing: border-box; }
  html, body {
    width: 750px;
    height: 1200px;
    overflow: hidden;
    background: var(--canvas-bg);
  }
  .canvas {
    width: 750px;
    height: 1200px;
    display: flex;
    flex-direction: column;
    align-items: center;
    justify-content: center;
    gap: 30px;
  }
  .label {
    position: relative;
    width: 560px;
    height: 540px;
    overflow: hidden;
  }
  .label--blue { background: var(--label-blue); }
  .label--teal { background: var(--label-teal); }

  .label__top-rule {
    position: absolute;
    top: 0; left: 0; right: 0;
    height: 8px;
    background: linear-gradient(90deg, var(--silver-mid), var(--silver-light) 30%, var(--silver-dark) 55%, var(--silver-light) 80%, var(--silver-mid));
  }
  .label__mark {
    position: absolute;
    top: 110px;
    left: 50%;
    width: 96px;
    height: 96px;
    margin-left: -48px;
    border-radius: 50%;
    background: linear-gradient(135deg, var(--silver-light), var(--silver-dark));
  }
  .label__name {
    position: absolute;
    top: 248px;
    left: 0; right: 0;
    text-align: center;
    font-family: "Josefin Slab", serif;
    font-weight: 300;
    font-size: 92px;
    line-height: 1;
    color: var(--text-white);
    letter-spacing: 1px;
  }
  .label__subline {
    position: absolute;
    top: 350px;
    left: 0; right: 0;
    text-align: center;
    font-family: "Raleway", sans-serif;
    font-weight: 300;
    font-size: 22px;
    color: var(--text-silver);
    letter-spacing: 0.5px;
  }
  .label__style-box {
    position: absolute;
    top: 386px;
    left: 50%;
    width: 180px;
    height: 72px;
    margin-left: -90px;
    border: 2px solid var(--text-silver);
    display: flex;
    align-items: center;
    justify-content: center;
    font-family: "Josefin Slab", serif;
    font-weight: 300;
    font-size: 52px;
    color: var(--text-silver);
    padding-top: 6px;
  }
  .label__band {
    position: absolute;
    left: 0; bottom: 0;
    width: 560px;
    height: 80px;
  }
  .label__band-text {
    position: absolute;
    bottom: 22px;
    font-family: "Raleway", sans-serif;
    font-weight: 300;
    color: var(--silver-light);
  }
  .label__origin { left: 46px; font-size: 24px; }
  .label__abv { right: 40px; bottom: 30px; font-size: 22px; }
</style>
</head>
<body>
<main class="canvas">

  <section class="label label--blue">
    <div class="label__top-rule"></div>
    <div class="label__mark" aria-hidden="true"></div>
    <h1 class="label__name">Lucenti</h1>
    <p class="label__subline">AGED IN OAK BARRELS</p>
    <p class="label__style-box">Brut</p>
    <svg class="label__band" viewBox="0 0 560 80" aria-hidden="true">
      <defs>
        <linearGradient id="bandBlue" x1="0" x2="1" y1="0" y2="0">
          <stop offset="0" stop-color="#b3b3b3"/>
          <stop offset="0.5" stop-color="#a2a2a2"/>
          <stop offset="1" stop-color="#b8b8b8"/>
        </linearGradient>
      </defs>
      <path d="M0 12 Q280 22 560 0 L560 80 L0 80 Z" fill="url(#bandBlue)"/>
    </svg>
    <span class="label__band-text label__origin">ITALIAN ORIGINAL</span>
    <span class="label__band-text label__abv">12% Alc.</span>
  </section>

  <section class="label label--teal">
    <div class="label__top-rule"></div>
    <div class="label__mark" aria-hidden="true"></div>
    <h2 class="label__name">Lucenti</h2>
    <p class="label__subline">AGED IN OAK BARRELS</p>
    <p class="label__style-box">Brut</p>
    <svg class="label__band" viewBox="0 0 560 80" aria-hidden="true">
      <defs>
        <linearGradient id="bandTeal" x1="0" x2="1" y1="0" y2="0">
          <stop offset="0" stop-color="#b3b3b3"/>
          <stop offset="0.5" stop-color="#a2a2a2"/>
          <stop offset="1" stop-color="#b8b8b8"/>
        </linearGradient>
      </defs>
      <path d="M0 12 Q280 22 560 0 L560 80 L0 80 Z" fill="url(#bandTeal)"/>
    </svg>
    <span class="label__band-text label__origin">ITALIAN ORIGINAL</span>
    <span class="label__band-text label__abv">12% Alc.</span>
  </section>

</main>
</body>
</html>
```